SEO AND WEB DESIGN COMPANY BUSINESS CARD DESIGN

I need an eye catching , simple business card design that will match my logo . I need 2 versions of it ( white background and black background) - SOME PEOPLE DID NOT GET IT AND SENDING US FRONT WHITE BACK WHITE VERSIONS WHICH IS NOT CORRECT.

ONE VERSION SHOULD BE BACK AND FRONT ALL BLACK , SECOND VERSION SHOULD BE BACK AND FRONT ALL WHITE

logo psd files are attached for both versions. The business card is going to have : First Name- Last name - position - phone numbers

```html
<!DOCTYPE html>
<html lang="en">
<head>
<meta charset="utf-8">
<title>Northvale Studio – Business Cards</title>
<link rel="stylesheet" href="https://fonts.googleapis.com/css2?family=Oswald:wght@500&family=Lato:wght@400;700&display=swap">
<style>
  :root {
    --stage: #141517;
    --card-dark: #1b1d20;
    --card-light: #ffffff;
    --accent: #3a8ff0;
    --ink-dark: #141414;
    --ink-light: #ffffff;
  }
  * { box-sizing: border-box; margin: 0; padding: 0; }
  html, body {
    width: 1200px;
    height: 912px;
    overflow: hidden;
    background: var(--stage);
  }
  .stage {
    position: relative;
    width: 1200px;
    height: 912px;
  }
  .card {
    position: absolute;
    left: 270px;
    width: 660px;
    height: 377px;
    overflow: hidden;
    box-shadow: 0 18px 40px rgba(0,0,0,0.55);
    --ink: var(--ink-dark);
  }
  .card::after {
    content: "";
    position: absolute;
    left: 0; right: 0; bottom: 0;
    height: 10px;
    background: var(--accent);
  }
  .card--dark { top: 54px; background: var(--card-dark); --ink: var(--ink-light); }
  .card--light { top: 481px; background: var(--card-light); --ink: var(--ink-dark); }

  .brand {
    position: absolute;
    left: 64px;
    top: 112px;
    display: flex;
    align-items: center;
    gap: 14px;
    white-space: nowrap;
    font-family: "Oswald", sans-serif;
    font-weight: 500;
    font-size: 44px;
    letter-spacing: 1px;
    text-transform: uppercase;
    line-height: 1;
    color: var(--ink);
  }
  .brand__dot {
    width: 30px;
    height: 30px;
    border-radius: 50%;
    background: var(--accent);
    flex: none;
  }

  .contact {
    position: absolute;
    left: 416px;
    top: 200px;
    font-family: "Lato", sans-serif;
    color: var(--ink);
    white-space: nowrap;
  }
  .contact__name {
    font-weight: 700;
    font-size: 27px;
    color: var(--accent);
    letter-spacing: -0.3px;
  }
  .contact__role {
    margin-top: 8px;
    margin-left: 22px;
    font-size: 17px;
  }
  .contact__phone {
    display: flex;
    align-items: center;
    gap: 10px;
    margin-top: 10px;
    margin-left: 22px;
    font-size: 20px;
  }
  .contact__phone svg { width: 16px; height: 16px; fill: var(--accent); }
</style>
</head>
<body>
<main class="stage">
  <section class="card card--dark" aria-label="Business card, all-black version">
    <div class="brand"><span class="brand__dot"></span>Northvale Studio</div>
    <div class="contact">
      <p class="contact__name">Marcus Hollaway</p>
      <p class="contact__role">Manager</p>
      <p class="contact__phone">
        <svg viewBox="0 0 24 24" aria-hidden="true"><path d="M6.6 10.8a15.1 15.1 0 0 0 6.6 6.6l2.2-2.2c.3-.3.7-.4 1-.2 1.1.4 2.3.6 3.6.6.6 0 1 .4 1 1V20c0 .6-.4 1-1 1A17 17 0 0 1 3 4c0-.6.4-1 1-1h3.5c.6 0 1 .4 1 1 0 1.3.2 2.5.6 3.6.1.3 0 .7-.2 1l-2.3 2.2z"/></svg>
        555 014 2290
      </p>
    </div>
  </section>

  <section class="card card--light" aria-label="Business card, all-white version">
    <div class="brand"><span class="brand__dot"></span>Northvale Studio</div>
    <div class="contact">
      <p class="contact__name">Marcus Hollaway</p>
      <p class="contact__role">Manager</p>
      <p class="contact__phone">
        <svg viewBox="0 0 24 24" aria-hidden="true"><path d="M6.6 10.8a15.1 15.1 0 0 0 6.6 6.6l2.2-2.2c.3-.3.7-.4 1-.2 1.1.4 2.3.6 3.6.6.6 0 1 .4 1 1V20c0 .6-.4 1-1 1A17 17 0 0 1 3 4c0-.6.4-1 1-1h3.5c.6 0 1 .4 1 1 0 1.3.2 2.5.6 3.6.1.3 0 .7-.2 1l-2.3 2.2z"/></svg>
        555 014 2290
      </p>
    </div>
  </section>
</main>
</body>
</html>
```